A Writer With A Website (Writes action/mysteries with a touch of romance thrown in)

I need a website. I am an unpublished writer. I own a domain and tried a bit to design one in Wordpress. I would like to be able to change out pictures, blog, and receive email. My fav color is orange (but not necessary in website) I like the font "Hello Stockholm" Probably 4 or five different pages. Attached is a poor scan of a business card.
Updates

Had a recent death in the family, my inspiration to get the site designed and also the reason I may need a few days.

I write books action mysteries. So far all take place in Wyoming. I realize there was not much info given. Pages: Home, Looking for representation, recommended reading and other things I like, Mirabel (a page dedicated to my daughter who just passed away), and other useful links. Probably shorter ways to say those, but you get the idea.

Thanks for the designs submitted. I know I gave very little direction. There are a few authors who write in Wyoming who are popular, RT Haskell, Dwight Fenner (Ashcroft Saga) I would argue that the main character in any of their books is Wyoming, or the West. No cliches. Cowboy hats, horses, not so good. For those outside the US, maybe do a serch on Wyoming and look at the pictures. I have photo's for possible use in my design, will post them tonight. Thanks all. -k-

I am not sure how much info gets added, how much the designer does and how I fill in the "blanks". Here is partial text for the "Mirabel" page: Over the years, our daughters’ friends overlapped one another and two or three became like daughters to Loreen and me. Some even became our friends as they grew into adulthood. One had a father who tried to committed suicide multiple times. After one attempt she asked him, “why?” He said, “I am glad you can’t understand why, only someone who can travel to that dark a place can understand why”. He was eventually successful. She shared that story with us on August 14th when our daughter Mirabel found that dark place in herself and took her life. We found a suicide note, then her body, then everything went into a fog. An hour or so later, my wife and I stood on the front lawn after the police interviews and watched as the corner slide a covered corpse into the white SUV with darkened windows. We stood there as the rain began to fall, and the sky sobbed with us. As they closed the back of the coroner’s Suburban, the rain fell harder and harder and a fireman guided us back into the house that will never be the same for us.

Target Market(s)

Currently trying to get an agent, this is to look like I have followers.

Number of Pages Required

5+ page

Font styles to use
Serif

Colors
f68e4e

Requirements
Nice to have
• I like orange (more of a burnt orange color) I am a big fan of Matthias Dorrel. A "feel" like that might be nice. I am from Wyoming, That rugged western culture shows up in all my writing.
Should not have
• Western Cliche,

```html
<!DOCTYPE html>
<html lang="en">
<head>
<meta charset="utf-8">
<title>Owen R. Hallam — Writer</title>
<link rel="stylesheet" href="https://fonts.googleapis.com/css2?family=Poppins:wght@300;400;500;600;700&family=Allura&display=swap">
<style>
:root{
  --orange:#f68e4e;
  --orange-deep:#e9773a;
  --sand:#d6c38f;
  --ink:#1f1f1f;
  --body:#555555;
  --muted:#999999;
  --paper:#ffffff;
  --mist:#f4f4f4;
  --line:#e6e6e6;
}
*{margin:0;padding:0;box-sizing:border-box}
html,body{width:1200px;height:4063px;overflow:hidden;background:var(--paper)}
body{position:relative;font-family:"Poppins",sans-serif;color:var(--ink)}
.abs{position:absolute}
.script{font-family:"Allura",cursive}

/* header */
.brand{left:34px;top:34px}
.brand-name{font-size:26px;font-weight:500;color:var(--orange);letter-spacing:.5px}
.brand-role{font-size:12px;font-weight:600;letter-spacing:2px;color:var(--ink);margin-top:2px;margin-left:40px}
.contact-top{top:18px;font-size:11px;color:var(--body);line-height:15px}
.contact-top span{display:block;color:var(--orange);font-size:9px}
.social-top{top:22px;display:flex;gap:8px;left:1110px}
.social-dot{width:22px;height:22px;border:1px solid var(--line);border-radius:50%}
.nav{top:78px;right:36px;display:flex;gap:30px;font-size:14px;font-weight:600;letter-spacing:.5px}

/* hero */
.hero-art{left:330px;top:141px;width:713px;height:482px;background:linear-gradient(135deg,#2f5aa0,#5f9b6a 45%,#3d6fb8 70%,#c9b25a)}
.hero-quote{left:154px;top:203px;width:510px;height:360px;background:linear-gradient(120deg,var(--orange-deep),#d9742f);color:#fff;padding:105px 40px 0 40px}
.hero-quote p{font-size:25px;line-height:36px;font-weight:500}
.hero-quote .qmark{font-size:56px;line-height:20px;font-weight:700;vertical-align:-14px;margin-right:6px}
.hero-quote cite{display:block;font-style:normal;font-weight:600;font-size:17px;margin-top:24px}
.hero-creature{left:500px;top:430px;width:140px;height:133px;background:radial-gradient(circle,#7a6a55,#a8612d)}

/* about */
.about-block{left:894px;top:623px;width:306px;height:582px;background:var(--orange)}
.about-frame{left:731px;top:726px;width:312px;height:425px;border:10px solid #f0f0f0;background:transparent}
.about-photo{left:677px;top:753px;width:315px;height:363px;background:linear-gradient(180deg,#e8e8e8,#6c6c6c 55%,#2a2a2a)}
.eyebrow{font-size:11px;color:var(--muted);letter-spacing:.5px;text-transform:uppercase}
.headline{font-size:38px;font-weight:700;line-height:47px;letter-spacing:.5px}
.headline span{background:linear-gradient(transparent 55%,#efefef 55%);padding-right:8px}
.para{font-size:13.5px;line-height:21px;color:var(--body)}
.more{font-size:12px;font-weight:600;letter-spacing:.5px;display:flex;align-items:center;gap:10px}
.more::after{content:"";width:54px;height:3px;background:var(--orange)}

/* banner */
.banner-back{left:230px;top:1281px;width:813px;height:399px;background:var(--sand)}
.banner{left:154px;top:1214px;width:813px;height:403px;background:linear-gradient(180deg,#5c5750,#9a948b 55%,#eceae6);display:flex;flex-direction:column;align-items:center;justify-content:center}
.banner h2{font-family:"Allura",cursive;font-weight:400;color:#fff;font-size:62px;margin-top:60px}
.btn-light{margin-top:18px;background:#fff;color:var(--ink);font-size:12px;letter-spacing:3px;padding:12px 26px}

/* story */
.story-photo{left:0;top:1739px;width:433px;height:439px;background:linear-gradient(135deg,#3a3a3a,#8b8b8b 50%,#d0d0d0)}
.story-panel{left:926px;top:1739px;width:55px;height:439px;background:#f1f1f1}
.story-person{left:981px;top:1739px;width:219px;height:439px;background:linear-gradient(160deg,#e0a074,#b0583e 60%,#6e3b2c)}

/* testimonials */
.quote-deco{left:22px;top:2310px;font-size:300px;line-height:300px;font-weight:700;color:#efefef}
.test-title{left:154px;top:2397px;font-size:24px;line-height:30px;font-weight:500}
.arrows{left:168px;top:2482px}
.test-block{left:466px;top:2262px;width:599px;height:333px;background:var(--orange)}
.card{top:2324px;width:290px;height:214px;background:#fff;box-shadow:0 6px 18px rgba(0,0,0,.12);padding:22px 20px}
.card::after{content:"";position:absolute;bottom:-14px;left:50%;margin-left:-12px;border:12px solid transparent;border-top-color:#fff;border-bottom:0;border-top-width:14px}
.card-head{display:flex;gap:14px;align-items:center;margin-bottom:16px}
.card-mark{width:38px;height:38px;background:#f2f2f2;color:var(--ink);font-weight:700;font-size:30px;text-align:center;line-height:46px}
.card-name{font-size:14px}
.card-role{font-size:11px;color:var(--muted)}
.card p{font-size:12.5px;line-height:19px;color:var(--body)}

/* news */
.news{left:0;top:2655px;width:1200px;height:821px;background:var(--mist)}
.news-title{left:0;width:1200px;top:2738px;text-align:center;font-size:50px}
.news-sub{left:0;width:1200px;top:2810px;text-align:center;font-size:16px;color:#444}
.news-card{background:#fff}
.news-big{left:144px;top:2880px;width:444px;height:414px}
.news-big .img{height:316px;background:linear-gradient(180deg,#2b2b2b,#7e7e7e 50%,#1b1b1b)}
.news-big h3{font-size:19px;font-weight:500;margin:26px 0 4px 22px}
.date{font-size:10px;color:var(--muted)}
.news-big .date{margin-left:22px}
.news-small{left:610px;width:447px;height:198px;display:flex}
.news-small .img{width:265px;height:198px}
.news-small .txt{padding:30px 0 0 20px}
.news-small h3{font-size:19px;font-weight:500;line-height:23px;margin-bottom:6px}
.btn-outline{left:523px;top:3350px;width:154px;height:38px;background:#fff;border:1px solid var(--line);font-size:12px;letter-spacing:3px;text-align:center;line-height:36px}

/* footer */
.foot-brand{left:0;width:1200px;top:3540px;text-align:center}
.foot-brand .brand-name{font-size:26px}
.foot-brand .brand-role{margin:0}
.foot-lead{left:0;width:1200px;top:3616px;text-align:center;font-size:22px;color:#333}
.foot-note{left:0;width:1200px;top:3656px;text-align:center;font-size:13px;color:var(--body)}
.subscribe{left:385px;top:3703px;width:428px;height:44px;border:1px solid var(--orange);border-radius:22px;display:flex;overflow:hidden}
.subscribe .field{flex:1;display:flex;align-items:center;gap:10px;padding-left:20px;font-size:12px;color:var(--muted)}
.subscribe .go{width:106px;background:var(--orange);color:#fff;font-size:12px;letter-spacing:2px;text-align:center;line-height:44px}
.info{top:3833px;width:220px;padding-left:26px}
.info h4{font-size:15px;font-weight:600;margin-bottom:2px}
.info p{font-size:12.5px;line-height:18px;color:var(--body)}
.info svg{position:absolute;left:0;top:3px}
.info-divider{top:3830px;width:1px;height:85px;background:var(--line)}
.info-social{display:flex;gap:8px;margin-top:8px}
.info-social i{width:26px;height:26px;border:1px solid #d8d8d8;display:block}
.copyright{left:0;width:1200px;top:3982px;text-align:center;font-size:11px;color:var(--muted)}
</style>
</head>
<body>

<header>
  <div class="abs brand">
    <div class="brand-name">Owen R. Hallam</div>
    <div class="brand-role">WRITER</div>
  </div>
  <div class="abs contact-top" style="left:846px"><span>Call Today</span>307.555.0142</div>
  <div class="abs contact-top" style="left:960px"><span>Email</span>info@owenhallam.com</div>
  <div class="abs social-top"><i class="social-dot"></i><i class="social-dot"></i></div>
  <nav class="abs nav"><span>ABOUT</span><span>STORY</span><span>NEWS</span><span>CONTACT</span></nav>
</header>

<section class="hero">
  <div class="abs hero-art" role="img" aria-label="Swirling blue and green expressionist landscape painting"></div>
  <div class="abs hero-quote">
    <p><span class="qmark">“</span>Great things are done by a series of small things brought together.</p>
    <cite>Matthias Dorrel</cite>
  </div>
  <div class="abs hero-creature" role="img" aria-label="Small owl peeking over the edge of the quote panel"></div>
</section>

<section class="about">
  <div class="abs about-block"></div>
  <div class="abs about-frame"></div>
  <div class="abs about-photo" role="img" aria-label="Black and white photo of a great tree with sunlight through its branches"></div>
  <div class="abs eyebrow" style="left:157px;top:800px">About Me</div>
  <h2 class="abs headline" style="left:157px;top:826px"><span>MEET THE BEST</span><br><span>IN THE BUSINESS</span></h2>
  <p class="abs para" style="left:182px;top:944px;width:410px">Lorem ipsum dolor sit amet, consectetur adipiscing elit. Donec rhoncus arcu nec mauris mattis, nec pulvinar orci bibendum. Etiam tincidunt erat eu metus egestas suscipit. Class aptent taciti sociosqu ad litora torquent per conubia nostra per inceptos himenaeos. Maecenas semper tincidunt purus.</p>
  <div class="abs more" style="left:182px;top:1068px">LEARN MORE</div>
</section>

<section class="craft">
  <div class="abs banner-back"></div>
  <div class="abs banner" role="img" aria-label="Cup of coffee beside hands turning the pages of an open book">
    <h2>Inviting a Good Copy Takes Words, Passion &amp; Skill</h2>
    <div class="btn-light">EXPLORE NOW</div>
  </div>
</section>

<section class="story">
  <div class="abs story-photo" role="img" aria-label="Black and white photo of hands joined in a fist bump over a desk"></div>
  <div class="abs eyebrow" style="left:456px;top:1782px">My Story</div>
  <h2 class="abs headline" style="left:466px;top:1810px"><span>REACH YOUR</span><br><span>POTENTIAL</span></h2>
  <p class="abs para" style="left:482px;top:1926px;width:420px">Cras a libero et justo ultricies rutrum vitae id augue. Cras cursus erat non pretium blandit. Cras eu sollicitudin urna. Sed ut ornare risus. In hac habitasse platea dictumst. In in mollis est. Sed eu elit id nulla porta consequat. Mauris sed dui ut tortor ultricies sagittis. Fusce cursus sem tellus vehicula.</p>
  <div class="abs more" style="left:482px;top:2043px">LEARN MORE</div>
  <div class="abs story-panel"></div>
  <div class="abs story-person" role="img" aria-label="Smiling man in a red shirt walking outdoors at sunset"></div>
</section>

<section class="testimonials">
  <div class="abs quote-deco">”</div>
  <h2 class="abs test-title">What Peoples<br>Are Saying</h2>
  <svg class="abs arrows" width="60" width="60" height="34" viewBox="0 0 60 34" aria-hidden="true">
    <polyline points="14,5 4,17 14,29" fill="none" stroke="#cccccc" stroke-width="2.5"/>
    <polyline points="46,5 56,17 46,29" fill="none" stroke="#222222" stroke-width="2.5"/>
  </svg>
  <div class="abs test-block"></div>
  <article class="abs card" style="left:385px">
    <div class="card-head"><div class="card-mark">“</div><div><div class="card-name">Nora Pilcher</div><div class="card-role">Business Woman</div></div></div>
    <p>Lorem ipsum dolor sit amet, consectetur adipiscing elit. Donec rhoncus arcu nec mauris mattis, nec pulvinar orci bibendum. Etiam tincidunt erat eu metus egestas suscipit. Class aptent taciti.</p>
  </article>
  <article class="abs card" style="left:699px">
    <div class="card-head"><div class="card-mark">“</div><div><div class="card-name">Tessa Wardell</div><div class="card-role">Home Maker</div></div></div>
    <p>Lorem ipsum dolor sit amet, consectetur adipiscing elit. Donec rhoncus arcu nec mauris mattis, nec pulvinar orci bibendum. Etiam tincidunt erat eu metus egestas suscipit. Class aptent taciti.</p>
  </article>
  <article class="abs card" style="left:1008px">
    <div class="card-head"><div class="card-mark">“</div><div><div class="card-name">Maren Colby</div><div class="card-role">Designer</div></div></div>
    <p>Lorem ipsum dolor sit amet, consectetur adipiscing elit. Donec rhoncus arcu nec mauris mattis, nec pulvinar orci bibendum. Etiam tincidunt erat eu metus egestas suscipit. Class aptent taciti.</p>
  </article>
</section>

<section>
  <div class="abs news"></div>
  <h2 class="abs news-title script" style="font-weight:400">Latest News and Updates</h2>
  <p class="abs news-sub">Let's chek out recent news</p>
  <article class="abs news-card news-big">
    <div class="img" role="img" aria-label="Black and white portrait of a bearded older man"></div>
    <h3>LOREM IPSUM DOLOR SIT AMETCTETUR</h3>
    <div class="date">Posted on Sep 06, 2018</div>
  </article>
  <article class="abs news-card news-small" style="top:2880px">
    <div class="img" role="img" aria-label="Older woman seated in warm evening light" style="background:linear-gradient(135deg,#3b2a22,#a0704a 60%,#d8b88a)"></div>
    <div class="txt"><h3>LOREM IPSUM<br>DOLOR SIT<br>AMETCTETUR</h3><div class="date">Posted on Sep 06, 2018</div></div>
  </article>
  <article class="abs news-card news-small" style="top:3096px">
    <div class="img" role="img" aria-label="Silhouette of a person standing against a hazy sunset sky" style="background:linear-gradient(180deg,#f1d9c2,#d59466 65%,#5e3a28)"></div>
    <div class="txt"><h3>LOREM IPSUM<br>DOLOR SIT<br>AMETCTETUR</h3><div class="date">Posted on Sep 06, 2018</div></div>
  </article>
  <div class="abs btn-outline">VIEW ALL</div>
</section>

<footer>
  <div class="abs foot-brand">
    <div class="brand-name">Owen R. Hallam</div>
    <div class="brand-role">WRITER</div>
  </div>
  <p class="abs foot-lead">Get latest news and updates to your mail box</p>
  <p class="abs foot-note">Sign up for our Newsletter and be the first to know about new products and promotions.</p>
  <div class="abs subscribe">
    <div class="field">
      <svg width="14" height="10" viewBox="0 0 14 10" aria-hidden="true"><rect x=".5" y=".5" width="13" height="9" fill="none" stroke="#f68e4e"/><polyline points=".5,.5 7,5.5 13.5,.5" fill="none" stroke="#f68e4e"/></svg>
      Enter your email address
    </div>
    <div class="go">SUBMIT</div>
  </div>

  <div class="abs info" style="left:171px">
    <svg width="14" height="18" viewBox="0 0 14 18" aria-hidden="true"><path d="M7 0C3 0 0 3 0 7c0 5 7 11 7 11s7-6 7-11c0-4-3-7-7-7z" fill="#f68e4e"/><circle cx="7" cy="7" r="2.5" fill="#fff"/></svg>
    <h4>Address</h4><p>418 Larkspur Rd<br>Cheyenne, WY 82009</p>
  </div>
  <div class="abs info-divider" style="left:405px"></div>
  <div class="abs info" style="left:420px">
    <svg width="16" height="12" viewBox="0 0 16 12" aria-hidden="true"><rect width="16" height="12" fill="#f68e4e"/><polyline points="0,0 8,6 16,0" fill="none" stroke="#fff" stroke-width="1.5"/></svg>
    <h4>Email</h4><p>info@owenhallam.com</p>
  </div>
  <div class="abs info-divider" style="left:662px"></div>
  <div class="abs info" style="left:677px">
    <svg width="14" height="16" viewBox="0 0 14 16" aria-hidden="true"><path d="M3 0l3 4-2 2c1 2 3 4 5 5l2-2 3 3-2 3C6 15 0 9 0 3z" fill="#f68e4e"/></svg>
    <h4>Phone</h4><p>307. 555. 0142</p>
  </div>
  <div class="abs info-divider" style="left:857px"></div>
  <div class="abs info" style="left:872px">
    <svg width="16" height="12" viewBox="0 0 16 12" aria-hidden="true"><rect width="16" height="12" fill="#f68e4e"/><polyline points="0,0 8,6 16,0" fill="none" stroke="#fff" stroke-width="1.5"/></svg>
    <h4>Social Media</h4><p>Join our social media</p>
    <div class="info-social"><i></i><i></i><i></i></div>
  </div>

  <p class="abs copyright">© 2018 Owen R. Hallam. All Rights Reserved.</p>
</footer>

</body>
</html>
```